WP website design (Pell)

We need a wordpress design for an established auction and real estate company based in Texas. The winning design will incorporate a professional color scheme with company logo in a clean layout. The design needs to consider that this will be developed on a responsive theme. Colors are those that will highlight the logo.

Reason: was waiting for updated logo

Industry/Entity Type

Real Estate

Font styles to use
Serif
Sans Serif

Requirements
Must have
• Navigation:
1) Home
2) Auctions
3) Online Auctions
4) Services
5) About Us
6) Contact us

Slideshow will be used - please use stock real estate photo. Tag line in the header - "Your Austin Auction Professionals!” Color of the site will be those in the logo and black.

Widgets - 1) Social media icons for twitter, facebook, linkedIn and Rss. 2) News & events blog, 3) Featured video, 4) Email Sign-up, 5) Testimonials

Company logo and contact info in the footer with attached logos too.
Nice to have
• Use of a drop down menu style - under 'Auctions'
1) Upcoming Auctions
2) Past Auctions

```html
<!DOCTYPE html>
<html lang="en">
<head>
<meta charset="utf-8">
<title>Pell Brothers Auction</title>
<link rel="stylesheet" href="https://fonts.googleapis.com/css2?family=Ubuntu:wght@400;500;700&family=Arimo:wght@400;700&display=swap">
<style>
:root{
  --navy:#2e3192;
  --red:#ed1c24;
  --red-dark:#b5121b;
  --ink:#333;
  --text:#222;
  --page:#f4f4f4;
  --footer:#262626;
  --white:#fff;
  --line:#d6d6d6;
}
*{box-sizing:border-box;margin:0;padding:0}
html,body{width:1080px;height:1200px;overflow:hidden}
body{position:relative;background:var(--page);font-family:"Arimo",Arial,sans-serif;color:var(--text)}
.abs{position:absolute}

.site-header{left:0;top:0;width:1080px;height:123px;background:var(--white)}
.brand{left:90px;top:56px;display:flex;align-items:center;gap:10px}
.brand .mark{width:18px;height:18px;border-radius:50%;background:var(--red)}
.brand .name{font-family:"Ubuntu",sans-serif;font-weight:500;font-size:26px;color:var(--ink);white-space:nowrap}
.social{left:694px;top:62px;display:flex;align-items:center;gap:9px}
.social .label{font-family:"Ubuntu",sans-serif;font-size:20px;color:var(--ink);margin-right:17px}
.social .dot{width:33px;height:33px;border-radius:50%}
.dot.one{background:#1d3a63}.dot.two{background:#1fa7e0}.dot.three{background:#f4900c}.dot.four{background:#b7b7b7}

.main-nav{left:0;top:123px;width:1080px;height:41px;border-top:2px solid var(--red);background:linear-gradient(#fff,#ececec)}
.main-nav ul{list-style:none;position:absolute;left:288px;top:10px;display:flex}
.main-nav li{font-size:13px;letter-spacing:.5px;color:var(--ink);padding:3px 23px;border-left:1px solid #bbb;white-space:nowrap}
.main-nav li:first-child{border-left:none}
.nav-pointer{left:328px;top:123px}

.hero-band{left:0;top:164px;width:1080px;height:430px}
.hero-frame{left:90px;top:188px;width:900px;height:315px;background:var(--white)}
.hero-photo{left:95px;top:194px;width:628px;height:302px;background:linear-gradient(180deg,#79b6ee 0%,#b9d9f2 30%,#7d6c5c 45%,#5e7d3a 70%,#7fb13c 100%)}
.signup{left:728px;top:194px;width:256px;height:302px;background:var(--red);padding:22px 19px}
.signup h2{font-family:"Ubuntu",sans-serif;font-weight:500;font-size:23px;color:var(--white);margin-bottom:18px;white-space:nowrap}
.field{height:31px;border-radius:16px;background:#fde8e9;border:2px solid #fff;font-size:13px;color:#444;padding:6px 12px;margin-bottom:18px}
.subscribe{float:right;margin-top:6px;background:linear-gradient(#333,#111);color:var(--white);font-family:"Ubuntu",sans-serif;font-weight:700;font-size:14px;padding:7px 15px;border-radius:7px}
.welcome{left:0;top:524px;width:1080px;text-align:center;color:var(--white);font-family:"Ubuntu",sans-serif;font-weight:500;font-size:25px;letter-spacing:.5px}

.section-title{left:89px;top:615px;font-family:"Ubuntu",sans-serif;font-weight:500;font-size:22px;color:var(--ink)}

.auction-card{width:637px;height:168px;background:var(--white);border:1px solid var(--line)}
.auction-card .thumb{position:absolute;left:7px;top:8px;width:98px;height:74px;background:linear-gradient(180deg,#8fbce0 0%,#e6e6e6 40%,#5a8a3a 75%,#4c7a2c 100%)}
.btn{position:absolute;left:6px;width:100px;height:27px;border-radius:5px;color:var(--white);font-weight:700;font-size:13px;display:flex;align-items:center;gap:9px;padding-left:12px}
.btn.details{top:92px;background:linear-gradient(#f0434a,var(--red-dark))}
.btn.photos{top:128px;background:linear-gradient(#4a4a4a,#1a1a1a)}
.btn svg{flex:none}
.auction-card .info{position:absolute;left:116px;top:10px;width:510px;font-size:11.5px;line-height:17px}
.info h3{font-weight:700;font-size:13px;letter-spacing:.6px;color:var(--red-dark);margin-bottom:1px}
.info b{font-weight:700}
.info .desc{margin-top:11px;line-height:16.5px}

.video{left:745px;top:650px;width:245px;height:176px;background:radial-gradient(circle at 50% 40%,#3a3a3a,#0c0c0c 70%)}
.video-controls{left:750px;top:803px;width:236px;height:17px;background:#e8e8e8;border:1px solid #999}

.testimonials{left:748px;top:856px;width:243px;height:202px;background:var(--white);border:1px solid var(--line);padding:11px 18px}
.testimonials h2{font-family:"Ubuntu",sans-serif;font-weight:700;font-size:21px;color:var(--navy);margin-bottom:10px;white-space:nowrap}
.quote{font-size:11px;font-style:italic;line-height:16.3px;color:#333;text-align:justify}
.quote .q{font-family:Georgia,serif;font-size:18px;font-weight:700}
.cite{position:absolute;right:66px;top:156px;text-align:right;font-size:11px;line-height:16px}
.cite a{color:var(--red-dark);font-style:italic;text-decoration:underline}
.avatar{position:absolute;right:13px;top:150px;width:37px;height:37px;border-radius:50%;background:linear-gradient(#b9c2c9,#6d7a84);border:2px solid #ddd}

.footer-rule{left:0;top:1106px;width:1080px;height:6px;background:var(--navy)}
.site-footer{left:0;top:1112px;width:1080px;height:88px;background:var(--footer);color:#eee}
.contact{position:absolute;left:99px;top:15px;font-size:11.5px;line-height:18px}
.contact .tel{margin-top:3px}
.badge{position:absolute;background:#8a8a8a}
.badge.wide{left:670px;top:26px;width:177px;height:38px;border-radius:4px}
.badge.square{left:863px;top:16px;width:50px;height:56px}
.badge.round{left:930px;top:18px;width:53px;height:53px;border-radius:50%}
</style>
</head>
<body>

<header class="site-header abs">
  <div class="brand abs">
    <span class="mark"></span>
    <span class="name">Pell Brothers Auction</span>
  </div>
  <div class="social abs">
    <span class="label">Social Media</span>
    <span class="dot one"></span><span class="dot two"></span><span class="dot three"></span><span class="dot four"></span>
  </div>
</header>

<nav class="main-nav abs">
  <ul>
    <li>HOME</li><li>AUCTIONS</li><li>ONLINE AUCTIONS</li><li>SERVICES</li><li>ABOUT US</li><li>CONTACT US</li>
  </ul>
</nav>
<svg class="nav-pointer abs" width="12" height="8"><polygon points="0,0 12,0 6,6" fill="#ed1c24"/></svg>

<svg class="hero-band abs" width="1080" height="430" viewBox="0 0 1080 430">
  <path d="M0 0H1080V365Q540 470 0 365Z" fill="#2e3192"/>
</svg>
<div class="hero-frame abs"></div>
<div class="hero-photo abs" role="img" aria-label="Stock photo of a large shingled country house with chimneys, a garden and a green lawn"></div>
<form class="signup abs">
  <h2>Newsletter Sign Up</h2>
  <div class="field">First Name</div>
  <div class="field">Last Name</div>
  <div class="field">Email Address</div>
  <div class="subscribe">SUBSCRIBE</div>
</form>
<h1 class="welcome abs">WELCOME TO PELL BROTHERS AUCTION</h1>

<h2 class="section-title abs">Types of Auctions</h2>

<article class="auction-card abs" style="left:90px;top:654px">
  <div class="thumb" role="img" aria-label="Crowd gathered on a lawn in front of a white house at an on-site auction"></div>
  <div class="btn details"><svg width="22" height="11"><rect x="0" y="0" width="9" height="11" fill="#fff"/><rect x="11" y="0" width="11" height="2" fill="#fff"/><rect x="11" y="4.5" width="11" height="2" fill="#fff"/><rect x="11" y="9" width="11" height="2" fill="#fff"/></svg>Details</div>
  <div class="btn photos"><svg width="20" height="16"><rect x="1" y="3" width="14" height="11" rx="1" fill="none" stroke="#fff" stroke-width="1.6"/><rect x="5" y="1" width="14" height="11" rx="1" fill="#333" stroke="#fff" stroke-width="1.6"/></svg>Photos</div>
  <div class="info">
    <h3>LIVE ON-SITE AUCTION</h3>
    <div><b>Begins:</b>&nbsp; Saturday, March 16, 2013 at 10:00 AM EDT</div>
    <div><b>Location:</b>&nbsp; 2290 Orchard Hill Road Lindale, TX 75771</div>
    <div>High Lift, simply dummy text of the printing and typesetting industry</div>
    <p class="desc">Makoto BS3F High Lift, simply dummy text of the printing and typesetting industry simply dummy text of the printing and typesetting industry 600 Series Fenwick tractor w/Harlow Loader, Dune buggy, 1207 KT Cutditioner: SHOP &amp; MISCELLANIOUS &amp; PORK PROCESSING ITEMS.</p>
  </div>
</article>

<div class="video abs" role="img" aria-label="Featured video player"></div>
<svg class="abs" style="left:846px;top:702px" width="44" height="44"><polygon points="12,6 36,22 12,38" fill="#e6e6e6"/></svg>
<svg class="video-controls abs" width="236" height="17">
  <polygon points="8,5 14,8.5 8,12" fill="#222"/>
  <text x="20" y="12" font-size="8" font-family="Arimo,sans-serif" fill="#222">00:00</text>
  <rect x="52" y="7" width="115" height="3" fill="#999"/>
  <text x="172" y="12" font-size="8" font-family="Arimo,sans-serif" fill="#222">00:00</text>
  <rect x="200" y="6" width="18" height="5" fill="#555"/>
  <rect x="224" y="5" width="7" height="7" fill="none" stroke="#222"/>
</svg>

<article class="auction-card abs" style="left:92px;top:856px">
  <div class="thumb" role="img" aria-label="Crowd gathered on a lawn in front of a white house at an on-site auction"></div>
  <div class="btn details"><svg width="22" height="11"><rect x="0" y="0" width="9" height="11" fill="#fff"/><rect x="11" y="0" width="11" height="2" fill="#fff"/><rect x="11" y="4.5" width="11" height="2" fill="#fff"/><rect x="11" y="9" width="11" height="2" fill="#fff"/></svg>Details</div>
  <div class="btn photos"><svg width="20" height="16"><rect x="1" y="3" width="14" height="11" rx="1" fill="none" stroke="#fff" stroke-width="1.6"/><rect x="5" y="1" width="14" height="11" rx="1" fill="#333" stroke="#fff" stroke-width="1.6"/></svg>Photos</div>
  <div class="info">
    <h3>LIVE ON-SITE AUCTION</h3>
    <div><b>Begins:</b>&nbsp; Saturday, March 16, 2013 at 10:00 AM EDT</div>
    <div><b>Location:</b>&nbsp; 2290 Orchard Hill Road Lindale, TX 75771</div>
    <div>High Lift, simply dummy text of the printing and typesetting industry</div>
    <p class="desc">Makoto BS3F High Lift, simply dummy text of the printing and typesetting industry simply dummy text of the printing and typesetting industry 600 Series Fenwick tractor w/Harlow Loader, Dune buggy, 1207 KT Cutditioner: SHOP &amp; MISCELLANIOUS &amp; PORK PROCESSING ITEMS.</p>
  </div>
</article>

<aside class="testimonials abs">
  <h2>Clients Testimonials</h2>
  <p class="quote"><span class="q">“</span> simply dummy text of the printing and typesetting industry. Lorem Ipsum has been the industry's standard dummy text ever since the 1500s, when an unknown&nbsp;<span class="q">”</span></p>
  <div class="cite">printing and typesetting<br><a>Marla Trent</a></div>
  <div class="avatar" role="img" aria-label="Client portrait"></div>
</aside>

<div class="footer-rule abs"></div>
<footer class="site-footer abs">
  <div class="contact">
    <div>Pell Brothers Auction Services</div>
    <div>418 Mill Creek Lane • Cedar Bend, TX 78612</div>
    <div class="tel">P: 512-555-0184 • F: 512-555-0185 • info@pellbrothersauctions.example</div>
  </div>
  <div class="badge wide"></div>
  <div class="badge square"></div>
  <div class="badge round"></div>
</footer>

</body>
</html>
```